r-brightlayer needs new website

need to get completely new updated site for r-brightlayer.com
general business concepts can be started from that site and I can offer specifick input about business operations and goals. would like to offer on-line ordering, service requests, and payments if possible.

```html
<!DOCTYPE html>
<html lang="en">
<head>
<meta charset="utf-8">
<title>R-Brightlayer | Imaging Solutions</title>
<link href="https://fonts.googleapis.com/css2?family=Poppins:wght@500;700&family=Raleway:wght@500;600;700&family=Lato:wght@400;700&display=swap" rel="stylesheet">
<style>
:root{
  --red:#e8202a;
  --ink:#1d1d1f;
  --text:#555a60;
  --muted:#9a9a9a;
  --line:#c9c9c9;
  --dark:#26282c;
  --white:#ffffff;
}
*{margin:0;padding:0;box-sizing:border-box}
html,body{width:797px;height:1200px;overflow:hidden;background:var(--white)}
body{position:relative;font-family:'Lato',sans-serif;color:var(--text)}
.abs{position:absolute}

/* header */
.site-header{position:absolute;left:0;top:0;width:797px;height:43px;background:var(--white);border-bottom:1px solid #e6e6e6}
.brand{position:absolute;left:150px;top:13px;display:flex;align-items:center;gap:5px;font-family:'Raleway',sans-serif;font-weight:700;font-size:11px;color:var(--ink)}
.brand-dot{width:12px;height:12px;border-radius:50%;background:var(--red)}
.main-nav a{position:absolute;top:17px;font-size:6.6px;color:#444;text-decoration:none;font-family:'Lato',sans-serif}
.main-nav a.active{color:var(--red)}
.nav-underline{position:absolute;left:316px;top:41px;width:30px;height:2px;background:var(--red)}
.phone{position:absolute;left:586px;top:16px;display:flex;align-items:center;gap:4px;font-size:6.8px;font-weight:700;color:#333}

/* hero */
.hero{position:absolute;left:0;top:43px;width:797px;height:315px;overflow:hidden}
.hero-photo{position:absolute;inset:0;background:linear-gradient(100deg,#cfd6d6 0%,#e9ecea 35%,#f3f4f2 55%,#dfe4e0 80%,#c9cfcd 100%)}
.hero-veil{position:absolute;inset:0;background:rgba(255,255,255,.35)}
.hero-kicker{position:absolute;left:0;width:797px;top:102px;text-align:center;font-family:'Poppins',sans-serif;font-weight:500;font-size:10px;color:var(--ink)}
.kicker-line{position:absolute;top:107px;width:40px;height:1px;background:var(--red)}
.hero-title{position:absolute;left:0;width:797px;top:118px;text-align:center;font-family:'Poppins',sans-serif;font-weight:700;font-size:23.5px;color:var(--red);letter-spacing:-.2px}
.hero-sub{position:absolute;left:0;width:797px;top:153px;text-align:center;font-family:'Poppins',sans-serif;font-weight:500;font-size:7px;color:var(--ink)}
.btn{position:absolute;display:flex;align-items:center;justify-content:center;font-family:'Poppins',sans-serif;font-weight:700;font-size:6.8px;text-transform:uppercase;text-decoration:none}
.btn-red{background:var(--red);color:var(--white)}
.btn-outline{border:1.5px solid var(--ink);color:var(--ink);background:rgba(255,255,255,.3)}

/* imaging */
.imaging-photo{position:absolute;left:104px;top:390px;width:294px;height:186px;background:radial-gradient(ellipse at 45% 45%,#3a3a3c 0%,#6a6a6c 30%,#e4e4e4 60%,#ffffff 80%)}
.eyebrow{font-family:'Raleway',sans-serif;font-weight:600;font-size:7.5px;color:var(--ink);text-transform:uppercase}
.section-title{font-family:'Raleway',sans-serif;font-weight:600;font-size:16px;text-transform:uppercase}
.rule{position:absolute;width:27px;height:1.5px;background:#bdbdbd}
.copy{font-size:7px;line-height:11.6px}

/* how we */
.how-band{position:absolute;left:0;top:598px;width:797px;height:274px;background:linear-gradient(100deg,#2d2f33 0%,#34363a 40%,#232427 70%,#1c1d20 100%)}
.how-frame{position:absolute;left:443px;top:657px;width:188px;height:174px;border:1px solid #7a1a1e}
.how-photo{position:absolute;left:459px;top:640px;width:188px;height:177px;background:linear-gradient(150deg,#f1efec 0%,#e2ddd7 45%,#8d8a88 75%,#bfbcb9 100%)}

/* applications */
.apps-title{position:absolute;left:0;width:797px;top:905px;text-align:center;font-family:'Raleway',sans-serif;font-weight:600;font-size:16px;color:var(--red)}
.app-card{position:absolute;top:950px;width:158px;height:231px;border:1px solid #e5e5e5;background:var(--white);text-align:center}
.app-photo{height:115px;background:radial-gradient(ellipse at 50% 55%,#6c7d96 0%,#2d466e 45%,#13284a 100%)}
.app-name{margin-top:13px;font-family:'Raleway',sans-serif;font-weight:700;font-size:9px;color:var(--ink);text-transform:uppercase}
.app-copy{margin:7px auto 0;width:135px;font-size:6.3px;line-height:10px;color:#777}
.app-card .btn{position:static;margin:12px auto 0;width:58px;height:17px;font-size:6.2px}
</style>
</head>
<body>

<header class="site-header">
  <div class="brand"><span class="brand-dot"></span>R-Brightlayer</div>
  <nav class="main-nav">
    <a class="active" href="#" style="left:322px">Home</a>
    <a href="#" style="left:362px">About Us</a>
    <a href="#" style="left:412px">Our Mission</a>
    <a href="#" style="left:471px">Applications</a>
    <a href="#" style="left:532px">Contact</a>
  </nav>
  <span class="nav-underline"></span>
  <div class="phone">
    <svg width="8" height="8" viewBox="0 0 24 24" fill="none" stroke="#e8202a" stroke-width="2.2"><path d="M22 16.9v3a2 2 0 0 1-2.2 2 19.8 19.8 0 0 1-8.6-3.1 19.5 19.5 0 0 1-6-6A19.8 19.8 0 0 1 2.1 4.2 2 2 0 0 1 4.1 2h3a2 2 0 0 1 2 1.7c.1 1 .4 1.9.7 2.8a2 2 0 0 1-.5 2.1L8 9.9a16 16 0 0 0 6 6l1.3-1.3a2 2 0 0 1 2.1-.4c.9.3 1.8.6 2.8.7a2 2 0 0 1 1.8 2z"/></svg>
    555-014-2236
  </div>
</header>

<section class="hero">
  <div class="hero-photo" role="img" aria-label="Office worker collecting documents from a desktop scanner in a bright office"></div>
  <div class="hero-veil"></div>
  <span class="kicker-line" style="left:284px"></span>
  <span class="kicker-line" style="left:474px"></span>
  <p class="hero-kicker">ONE DEVICE FOR ALL YOUR</p>
  <h1 class="hero-title">BRANCH PLATFORM &amp; SALES DESK</h1>
  <p class="hero-sub">DOCUMENTATION NEEDS</p>
  <a class="btn btn-red" href="#" style="left:329px;top:192px;width:65px;height:19px">About Us</a>
  <a class="btn btn-outline" href="#" style="left:403px;top:192px;width:65px;height:19px">Contact Us</a>
</section>

<section class="imaging">
  <div class="imaging-photo" role="img" aria-label="Black desktop printer feeding a sheet of paper"></div>
  <p class="abs eyebrow" style="left:423px;top:397px">Imaging Solutions</p>
  <h2 class="abs section-title" style="left:422px;top:407px;color:var(--red)">For Your Business</h2>
  <span class="rule" style="left:422px;top:433px"></span>
  <p class="abs copy" style="left:422px;top:445px;width:220px">R-BRIGHTLAYER strives to be the leading provider of cost-effective solutions to the Retail, Wholesale and Banking Marketplace. Our experience in supplying complete software, hardware, and turnkey systems enables us to provide a system that fits your needs, we don't believe in trying to change your operations to fit our products.</p>
  <a class="btn btn-red" href="#" style="left:422px;top:514px;width:65px;height:19px">Read More</a>
</section>

<section class="how">
  <div class="how-band" role="img" aria-label="Dimmed close-up of hands operating an office scanner"></div>
  <p class="abs eyebrow" style="left:148px;top:663px;color:var(--white)">How We</p>
  <h2 class="abs section-title" style="left:148px;top:673px;color:var(--white)">Do Business</h2>
  <span class="rule" style="left:148px;top:698px;background:#8a8a8a"></span>
  <p class="abs copy" style="left:148px;top:710px;width:270px;color:#e4e4e4">R-BRIGHTLAYER strives to be the leading provider of cost-effective software, hardware, and turnkey solutions to the Business, Utility, and Banking Marketplace.</p>
  <p class="abs copy" style="left:148px;top:746px;width:270px;color:#e4e4e4">We know that technology is extremely important in giving our customers a competitive advantage. We also realize that the need to keep up with technology is not in the everyday realm of many business owners expertise so we can offer significant value in providing complete solutions with ongoing support.</p>
  <div class="how-frame"></div>
  <div class="how-photo" role="img" aria-label="Smiling businesswoman feeding documents into a multifunction scanner"></div>
</section>

<section class="applications">
  <h2 class="apps-title">APPLICATIONS</h2>
  <span class="rule" style="left:385px;top:931px"></span>

  <article class="app-card" style="left:148px">
    <div class="app-photo" role="img" aria-label="Multi-function cheque scanner with receipt printer on a blue backdrop"></div>
    <h3 class="app-name">Multi-Function Options</h3>
    <p class="app-copy">Lorem Ipsum is simply dummy text of printing and typesetting industry. Lorem Ipsum has been the industry's standard dummy text ever since the 1500s.</p>
    <a class="btn btn-red" href="#">Read More</a>
  </article>

  <article class="app-card" style="left:319px">
    <div class="app-photo" role="img" aria-label="Compact grey document scanner on a blue backdrop"></div>
    <h3 class="app-name">Clarity Scan</h3>
    <p class="app-copy">Lorem Ipsum is simply dummy text of printing and typesetting industry. Lorem Ipsum has been the industry's standard dummy text ever since the 1500s.</p>
    <a class="btn btn-red" href="#">Read More</a>
  </article>

  <article class="app-card" style="left:489px">
    <div class="app-photo" role="img" aria-label="Black sheet-fed scanner with blue input tray on a blue backdrop"></div>
    <h3 class="app-name">Swiftfeed</h3>
    <p class="app-copy">Lorem Ipsum is simply dummy text of printing and typesetting industry. Lorem Ipsum has been the industry's standard dummy text ever since the 1500s.</p>
    <a class="btn btn-red" href="#">Read More</a>
  </article>
</section>

</body>
</html>
```